New Business Card Design Project

Use the flyer uploaded and website www.brightoakbuilders.com for inspiration.
List Our Services on Backside of business cards
Martin Hollis
Harborline Renovations Inc.
Licensed General Contractors
858-471-9063

Contact Information for Business Card

Use the flyer uploaded and website www.brightoakbuilders.com for inspiration. List Our Services on Backside of business cards Martin Hollis Harborline Renovations Inc. Licensed General Contractors 858-471-9063

```html
<!DOCTYPE html>
<html lang="en">
<head>
<meta charset="utf-8">
<title>Harborline Renovations – Business Card</title>
<link rel="stylesheet" href="https://fonts.googleapis.com/css2?family=Oswald:wght@300;400;500;600;700&display=swap">
<style>
  :root {
    --backdrop: #a9a9a9;
    --card-black: #131313;
    --card-white: #ffffff;
    --accent-blue: #3a82c4;
    --accent-red: #e3222a;
    --text-grey: #6e6e6e;
    --text-white: #ffffff;
    --photo-living-a: #dfe3e6;
    --photo-living-b: #9fa6ab;
    --photo-kitchen-a: #e9c79a;
    --photo-kitchen-b: #a8672f;
  }
  * { margin: 0; padding: 0; box-sizing: border-box; }
  html, body { width: 1200px; height: 1000px; overflow: hidden; }
  body { background: var(--backdrop); position: relative; font-family: "Oswald", sans-serif; }

  .card {
    position: absolute; left: 294px; width: 613px; height: 352px;
    background: var(--card-black);
    box-shadow: 0 14px 34px rgba(0,0,0,0.35);
  }
  .card--front { top: 119px; }
  .card--back { top: 531px; }
  .card__art { position: absolute; left: 0; top: 0; width: 613px; height: 352px; overflow: visible; }

  /* Front */
  .brand {
    position: absolute; left: 30px; top: 110px; width: 212px;
    display: flex; align-items: center; justify-content: center; gap: 8px;
    color: var(--text-white);
  }
  .brand__mark {
    width: 14px; height: 14px; background: var(--text-white); flex: none;
  }
  .brand__name {
    font-weight: 400; font-size: 18px; line-height: 24px; letter-spacing: 1px;
    white-space: nowrap;
  }
  .contact-name {
    position: absolute; left: 36px; top: 250px;
    color: var(--accent-red); font-weight: 600; font-size: 32px; line-height: 1;
  }
  .contact-role {
    position: absolute; left: 36px; top: 291px;
    color: var(--text-grey); font-weight: 300; font-size: 14.5px; line-height: 18px;
  }

  /* Back */
  .services-tag {
    position: absolute; left: 0; top: 24px; width: 176px; height: 24px;
    background: var(--accent-blue);
    clip-path: polygon(0 0, 100% 0, 95% 100%, 0 100%);
    color: var(--text-white); font-weight: 500; font-size: 16px; letter-spacing: 2px;
    line-height: 24px; padding-left: 13px;
  }
  .services-list {
    position: absolute; left: 14px; top: 62px; list-style: none;
    color: var(--text-white); font-weight: 400; font-size: 17px; line-height: 24px;
  }
  .services-list li { display: flex; align-items: center; letter-spacing: -0.2px; }
  .services-list svg { width: 17px; height: 17px; margin-right: 8px; flex: none; }
  .divider {
    position: absolute; left: 14px; top: 270px; width: 182px; height: 2px;
    background: var(--accent-red);
  }
  .phone {
    position: absolute; left: 12px; top: 280px; display: flex; align-items: center;
    color: var(--text-white); font-weight: 600; font-size: 27px; line-height: 36px;
  }
  .phone svg { width: 22px; height: 22px; margin-right: 5px; }
  .website {
    position: absolute; left: 12px; top: 313px;
    color: var(--text-white); font-weight: 300; font-size: 21px; line-height: 28px;
  }
</style>
</head>
<body>

<section class="card card--front">
  <svg class="card__art" viewBox="0 0 613 352">
    <defs>
      <linearGradient id="livingTones" x1="0" y1="0" x2="1" y2="1">
        <stop offset="0" stop-color="var(--photo-living-a)"/>
        <stop offset="1" stop-color="var(--photo-living-b)"/>
      </linearGradient>
    </defs>
    <polygon points="0,163 613,341 613,352 0,352" fill="var(--card-white)"/>
    <polygon points="135,202 604,72 604,338" fill="url(#livingTones)" role="img" aria-label="Photo of a bright modern living room with a grey sectional sofa and white kitchen"/>
    <polyline points="128,202 609,64 609,345" fill="none" stroke="var(--accent-blue)" stroke-width="5"/>
  </svg>
  <div class="brand">
    <span class="brand__mark"></span>
    <span class="brand__name">HARBORLINE RENOVATIONS</span>
  </div>
  <h1 class="contact-name">Martin Hollis</h1>
  <p class="contact-role">Harborline Renovations Inc.<br>Licensed General Contractors</p>
</section>

<section class="card card--back">
  <svg class="card__art" viewBox="0 0 613 352">
    <defs>
      <linearGradient id="kitchenTones" x1="0" y1="0" x2="1" y2="1">
        <stop offset="0" stop-color="var(--photo-kitchen-a)"/>
        <stop offset="1" stop-color="var(--photo-kitchen-b)"/>
      </linearGradient>
    </defs>
    <polygon points="261,105 591,14 591,352 261,352" fill="url(#kitchenTones)" role="img" aria-label="Photo of a kitchen renovation blending timber framing into a finished white kitchen"/>
    <polyline points="263,366 263,105 590,12 590,366" fill="none" stroke="var(--accent-blue)" stroke-width="5"/>
  </svg>

  <div class="services-tag">SPECIALIZING IN:</div>
  <ul class="services-list">
    <li><svg viewBox="0 0 20 20"><circle cx="10" cy="10" r="8" fill="none" stroke="var(--accent-red)" stroke-width="2"/><path d="M6 10l3 3 5-6" fill="none" stroke="var(--accent-red)" stroke-width="2"/></svg>Remodel: Kitchen &amp; Bath</li>
    <li><svg viewBox="0 0 20 20"><circle cx="10" cy="10" r="8" fill="none" stroke="var(--accent-red)" stroke-width="2"/><path d="M6 10l3 3 5-6" fill="none" stroke="var(--accent-red)" stroke-width="2"/></svg>Painting: Interior &amp; Exterior</li>
    <li><svg viewBox="0 0 20 20"><circle cx="10" cy="10" r="8" fill="none" stroke="var(--accent-red)" stroke-width="2"/><path d="M6 10l3 3 5-6" fill="none" stroke="var(--accent-red)" stroke-width="2"/></svg>Flooring: Carpet, Vinyl, Wood</li>
    <li><svg viewBox="0 0 20 20"><circle cx="10" cy="10" r="8" fill="none" stroke="var(--accent-red)" stroke-width="2"/><path d="M6 10l3 3 5-6" fill="none" stroke="var(--accent-red)" stroke-width="2"/></svg>Window &amp; Door Replacement</li>
    <li><svg viewBox="0 0 20 20"><circle cx="10" cy="10" r="8" fill="none" stroke="var(--accent-red)" stroke-width="2"/><path d="M6 10l3 3 5-6" fill="none" stroke="var(--accent-red)" stroke-width="2"/></svg>Plumbing: Repairs &amp; Upgrades</li>
    <li><svg viewBox="0 0 20 20"><circle cx="10" cy="10" r="8" fill="none" stroke="var(--accent-red)" stroke-width="2"/><path d="M6 10l3 3 5-6" fill="none" stroke="var(--accent-red)" stroke-width="2"/></svg>Deck &amp; Patio Construction</li>
    <li><svg viewBox="0 0 20 20"><circle cx="10" cy="10" r="8" fill="none" stroke="var(--accent-red)" stroke-width="2"/><path d="M6 10l3 3 5-6" fill="none" stroke="var(--accent-red)" stroke-width="2"/></svg>Water &amp; Mold Damage</li>
    <li><svg viewBox="0 0 20 20"><circle cx="10" cy="10" r="8" fill="none" stroke="var(--accent-red)" stroke-width="2"/><path d="M6 10l3 3 5-6" fill="none" stroke="var(--accent-red)" stroke-width="2"/></svg>Garage Renovation</li>
  </ul>
  <div class="divider"></div>
  <p class="phone"><svg viewBox="0 0 24 24"><circle cx="12" cy="12" r="11" fill="var(--accent-red)"/><path d="M8.2 6.5l2 2.3-1.1 1.5c.8 1.7 2 2.9 3.6 3.7l1.5-1.1 2.3 2-1.2 1.8c-4.3-.6-7.9-4.2-8.5-8.5z" fill="var(--card-black)"/></svg>858-471-9063</p>
  <p class="website">BrightOakBuilders.com</p>
</section>

</body>
</html>
```